Brin-well Tide Port Custom Brokers Limited

Name: Loranda Pascoe
Title: Customs Broker
Address: Shop 9 Fernvale Commercial Complex
227-229 Marrow Lane
Kingston 8
Telephone: (876)
Email: tideportbrin@quillmail.example

```html
<!DOCTYPE html>
<html lang="en">
<head>
<meta charset="utf-8">
<title>Brin-well Tide Port – Business Card</title>
<link href="https://fonts.googleapis.com/css2?family=Poppins:wght@300;400;600;700&display=swap" rel="stylesheet">
<style>
  :root{
    --navy:#0f1d3a;
    --navy-deep:#0b1730;
    --gold:#d99a17;
    --silver:#c9ced6;
    --paper:#f7f8fa;
    --stage:#e4e7ec;
    --ink-soft:#5a6272;
    --light-text:#e6e9ef;
  }
  html,body{margin:0;padding:0;}
  body{
    width:1200px;height:970px;overflow:hidden;
    background:var(--stage);
    font-family:'Poppins',sans-serif;
    position:relative;
  }
  .business-card{
    position:absolute;left:80px;top:187px;
    width:1040px;height:596px;
    border-radius:26px;overflow:hidden;
    background:var(--paper);
    box-shadow:0 18px 40px rgba(15,29,58,.22);
  }
  .card-art{position:absolute;inset:0;}
  .brand{
    position:absolute;left:40px;top:56px;width:500px;
    text-align:center;
  }
  .brand-mark{
    width:120px;height:120px;border-radius:50%;
    background:var(--navy);margin:0 auto 36px;
  }
  .brand-name{
    font-weight:600;font-size:40px;letter-spacing:.5px;
    color:var(--navy);line-height:1;margin:0;
    text-transform:uppercase;
  }
  .brand-sub{
    font-weight:400;font-size:21px;letter-spacing:11px;line-height:1;
    color:var(--ink-soft);margin-top:10px;
  }
  .holder{
    position:absolute;right:48px;top:78px;text-align:right;
  }
  .holder-name{
    font-weight:700;font-size:32px;color:var(--navy);
    text-transform:uppercase;margin:0;line-height:1.1;
  }
  .holder-title{
    font-weight:400;font-size:24px;color:var(--gold);margin-top:2px;
  }
  .contacts{
    position:absolute;right:48px;top:301px;
    list-style:none;margin:0;padding:0;text-align:right;
    color:var(--light-text);font-weight:300;font-size:24px;
  }
  .contacts li{display:flex;justify-content:flex-end;align-items:center;height:33.5px;gap:12px;}
  .contacts .accent{color:var(--gold);}
  .contact-icon{width:26px;height:26px;flex:none;}
  .address{
    position:absolute;right:48px;top:444px;text-align:right;
    color:var(--silver);font-weight:300;font-size:24px;line-height:33px;
  }
  .tagline{
    position:absolute;right:48px;top:525px;
    color:var(--silver);font-weight:600;font-size:22px;
    text-transform:uppercase;letter-spacing:.3px;
  }
</style>
</head>
<body>
<section class="business-card">
  <svg class="card-art" viewBox="0 0 1040 596" width="1040" height="596" aria-hidden="true">
    <defs>
      <linearGradient id="silverBand" x1="0" y1="0" x2="1" y2="0">
        <stop offset="0" stop-color="#dfe3e9"/>
        <stop offset=".5" stop-color="#b7bec9"/>
        <stop offset="1" stop-color="#e8ebef"/>
      </linearGradient>
      <linearGradient id="goldSweep" x1="0" y1="1" x2="1" y2="0">
        <stop offset="0" stop-color="#b97f0c"/>
        <stop offset="1" stop-color="#e8ad2e"/>
      </linearGradient>
    </defs>
    <path d="M80 596 C 280 545, 440 395, 615 295 C 760 228, 910 222, 1040 240 L1040 596 Z" fill="url(#silverBand)"/>
    <path d="M110 596 C 300 560, 450 420, 620 320 C 760 250, 900 240, 1040 262 L1040 596 Z" fill="var(--navy-deep)"/>
    <path d="M175 505 C 380 440, 520 305, 700 255 C 820 226, 920 224, 980 232" fill="none" stroke="var(--navy)" stroke-width="10" stroke-linecap="round"/>
    <path d="M178 470 C 300 455, 420 400, 492 325 C 440 400, 330 460, 185 490 Z" fill="url(#goldSweep)"/>
  </svg>

  <div class="brand">
    <div class="brand-mark"></div>
    <p class="brand-name">Brin-well Tide Port</p>
    <div class="brand-sub">Custom Brokers Ltd.</div>
  </div>

  <div class="holder">
    <p class="holder-name">Loranda Pascoe</p>
    <div class="holder-title">Customs Broker</div>
  </div>

  <ul class="contacts">
    <li>(876) 555-0148
      <svg class="contact-icon" viewBox="0 0 26 26"><circle cx="13" cy="13" r="12" fill="var(--gold)"/><rect x="9" y="6" width="8" height="14" rx="1.5" fill="none" stroke="var(--navy)" stroke-width="2"/></svg></li>
    <li>(876) 555-0162
      <svg class="contact-icon" viewBox="0 0 26 26"><circle cx="13" cy="13" r="12" fill="var(--gold)"/><path d="M7 10 Q13 5 19 10 L17 12 L15 10 L11 10 L9 12 Z M8 14 H18 V19 H8 Z" fill="var(--navy)"/></svg></li>
    <li>tideportbrin@quillmail.example
      <svg class="contact-icon" viewBox="0 0 26 26"><circle cx="13" cy="13" r="12" fill="var(--gold)"/><rect x="7" y="8.5" width="12" height="9" fill="var(--navy)"/><path d="M7 8.5 L13 13.5 L19 8.5" fill="none" stroke="var(--gold)" stroke-width="1.3"/></svg></li>
    <li><span>www.<span class="accent">tideportbrin</span>.example</span>
      <svg class="contact-icon" viewBox="0 0 26 26"><circle cx="13" cy="13" r="12" fill="var(--gold)"/><circle cx="13" cy="13" r="6.5" fill="none" stroke="var(--navy)" stroke-width="1.6"/><path d="M6.5 13 H19.5 M13 6.5 V19.5" stroke="var(--navy)" stroke-width="1.4"/></svg></li>
  </ul>

  <div class="address">Shop 9 Fernvale Commercial Complex<br>227-229 Marrow Lane, Kingston 8</div>
  <div class="tagline">Clearing cargo smoothly across every port</div>
</section>
</body>
</html>
```